Boutique Fitness Facility needs a new meal plan design that is as hot as our workouts!

We are about to host our 6 week Coral Tide program and we need to have a great looking meal plan handout created that we can give to all of our participants.

I have attached an example of our current full meal plan, for a reference only.

As in the example I've provided, I'd like to have certain areas color coded such as the proteins being Blue, Fats -yellow, Carbs - orange and veggies- green.

These colors will corollate to the Breakfast - snack - lunch - snack - Dinner graph that I've provided and would like to have added to the new handout.

I would like our logo placed at the top and beneath the logo have the text "Coral Tide Challenge"

The flyer should be of a summer influence in colors and design and
All text should be easy to read.

Thank you and I look forward to seeing your design!

```html
<!DOCTYPE html>
<html lang="en">
<head>
<meta charset="UTF-8">
<title>Coral Tide Challenge – Meal Plan</title>
<link rel="stylesheet" href="https://fonts.googleapis.com/css2?family=Archivo:wght@600;800;900&family=Barlow:wght@400;500;600;700;800&display=swap">
<style>
  :root{
    --backdrop:#9a9a9a;
    --navy:#1d1a63;
    --navy-deep:#151247;
    --violet:#3a1f8a;
    --protein:#3d52a8;
    --fat:#f6cc12;
    --carbs:#f08c1e;
    --veg:#55b848;
    --yellow:#f6d313;
    --white:#ffffff;
    --ink:#1c1c22;
    --note-blue:#213c8f;
  }
  *{box-sizing:border-box;margin:0;padding:0}
  html,body{width:991px;height:1200px;overflow:hidden;background:var(--backdrop)}
  body{font-family:"Barlow",Arial,sans-serif;color:var(--white)}
  .flyer{
    position:absolute;left:32.7px;top:0;width:668px;height:866px;
    transform:scale(1.3857);transform-origin:0 0;overflow:hidden;
    background:linear-gradient(180deg,#2a2060 0%,var(--navy) 55%,var(--navy-deep) 78%,var(--violet) 100%);
  }
  .hero-photo{
    position:absolute;left:0;top:0;width:668px;height:560px;
    background:linear-gradient(180deg,rgba(120,84,80,.55) 0%,rgba(74,52,92,.55) 40%,rgba(29,26,99,0) 100%);
  }
  .brand{position:absolute;top:36px;left:0;width:100%;text-align:center}
  .brand-name{font-family:"Archivo",Arial,sans-serif;font-weight:900;font-size:46px;letter-spacing:-1px;color:var(--white);line-height:1}
  .brand-tag{margin-top:6px;font-size:7.5px;font-weight:700;letter-spacing:2.4px;color:var(--yellow)}
  .title-band{
    position:absolute;left:92px;top:128px;width:512px;height:38px;background:var(--yellow);
    transform:rotate(-2deg);display:flex;align-items:center;justify-content:center;
  }
  .title-band span{font-family:"Archivo",Arial,sans-serif;font-weight:800;font-size:22px;letter-spacing:2px;color:var(--white);text-shadow:0 1px 2px rgba(0,0,0,.35)}
  .field{position:absolute;top:186px;font-family:"Archivo",Arial,sans-serif;font-weight:800;font-size:15px;color:var(--yellow)}
  .field-line{position:absolute;top:201px;height:1px;background:rgba(255,255,255,.7)}
  .food-col{position:absolute;top:238px;width:135px;height:247px;border-radius:14px}
  .food-col.protein{left:35px;background:var(--protein)}
  .food-col.fat{left:190px;background:var(--fat)}
  .food-col.carbs{left:343px;background:var(--carbs)}
  .food-col.veg{left:497px;background:var(--veg)}
  .col-icon{position:absolute;top:-19px;left:50%;margin-left:-18px;width:36px;height:36px;border-radius:50%;background:var(--white);border:2px solid var(--navy)}
  .col-icon i{position:absolute;left:9px;top:9px;width:14px;height:14px;border-radius:50%}
  .col-head{
    position:absolute;top:32px;left:-6px;width:147px;height:30px;background:var(--white);
    font-family:"Archivo",Arial,sans-serif;font-weight:800;font-size:17px;letter-spacing:1.6px;color:var(--ink);
    display:flex;align-items:center;justify-content:center;
  }
  .food-list{position:absolute;top:68px;left:10px;right:6px;list-style:none}
  .food-list li{position:relative;padding-left:15px;font-size:8px;line-height:10px;margin-bottom:5.3px}
  .fat .food-list li{color:var(--ink);margin-bottom:7px}
  .carbs .food-list li{margin-bottom:7px}
  .veg .food-list li{margin-bottom:7.6px}
  .food-list li svg{position:absolute;left:0;top:1px;width:8px;height:8px}
  .note{
    position:absolute;left:117px;top:487px;width:452px;height:25px;background:var(--white);border-radius:0 0 10px 10px;
    display:flex;align-items:center;color:var(--ink);font-size:8px;
  }
  .note b{font-family:"Archivo",Arial,sans-serif;font-weight:800;font-size:11px;color:var(--note-blue);margin:0 20px 0 14px}
  .note span{margin-right:38px}
  .meal-wheel{position:absolute;top:540px;width:120px;height:120px;overflow:visible}
  .meal-wheel text{font-family:"Barlow",Arial,sans-serif}
  .snack{position:absolute;top:566px;width:70px;text-align:center}
  .snack svg{display:block;margin:0 auto 4px}
  .snack-tag{display:inline-block;background:var(--veg);padding:1px 9px;font-family:"Archivo",Arial,sans-serif;font-weight:800;font-size:11px;letter-spacing:1px}
  .snack p{margin-top:5px;font-size:7.5px;line-height:10px}
  .fuel-band{
    position:absolute;left:8px;top:678px;width:214px;height:40px;background:var(--yellow);transform:rotate(-1deg);
    display:flex;flex-direction:column;justify-content:center;padding-left:28px;
    font-family:"Archivo",Arial,sans-serif;font-weight:900;font-size:15px;line-height:15px;color:var(--white);text-shadow:0 1px 2px rgba(0,0,0,.4)
  }
  .fuel-copy{position:absolute;left:233px;top:680px;width:420px;font-size:13px;line-height:17px;font-weight:500}
  .tips{position:absolute;left:37px;top:733px;width:593px;height:102px;background:var(--white);border-radius:8px;display:flex;overflow:hidden}
  .tip{position:relative;flex:1;padding:8px 6px 0 6px;color:var(--ink);border-right:1px solid #d8d8de}
  .tip:last-child{border-right:none}
  .tip h3{font-size:9.5px;line-height:9.5px;font-weight:800;width:78px;height:22px}
  .tip p{font-size:7.6px;line-height:10.4px}
  .tip-num{position:absolute;top:0;right:0;width:26px;height:17px;background:var(--yellow);border-radius:0 0 0 6px;font-family:"Archivo",Arial,sans-serif;font-weight:800;font-size:12px;text-align:center;line-height:17px;color:var(--ink)}
</style>
</head>
<body>
<main class="flyer">
  <div class="hero-photo" role="img" aria-label="Photo of a smiling group of training members standing together in a gym"></div>

  <header class="brand">
    <div class="brand-name">PulseForge</div>
    <div class="brand-tag">PERSONAL GROUP TRAINING</div>
  </header>

  <div class="title-band"><span>CORAL TIDE CHALLENGE</span></div>

  <div class="field" style="left:40px">NAME</div>
  <div class="field-line" style="left:92px;width:253px"></div>
  <div class="field" style="left:367px">MEAL PLAN</div>
  <div class="field-line" style="left:473px;width:152px"></div>

  <section class="food-col protein">
    <div class="col-icon" role="img" aria-label="Meat and poultry icon"><i style="background:#e0524a"></i></div>
    <h2 class="col-head">PROTEIN</h2>
    <ul class="food-list">
      <li><svg viewBox="0 0 8 8"><rect x=".5" y=".5" width="7" height="7" fill="none" stroke="#f6d313"/><path d="M1.8 4l1.6 1.6L6.4 2" fill="none" stroke="#f6d313" stroke-width="1.1"/></svg>4-6 oz Chicken Breast</li>
      <li><svg viewBox="0 0 8 8"><rect x=".5" y=".5" width="7" height="7" fill="none" stroke="#f6d313"/><path d="M1.8 4l1.6 1.6L6.4 2" fill="none" stroke="#f6d313" stroke-width="1.1"/></svg>4-6oz Turkey Breast</li>
      <li><svg viewBox="0 0 8 8"><rect x=".5" y=".5" width="7" height="7" fill="none" stroke="#f6d313"/><path d="M1.8 4l1.6 1.6L6.4 2" fill="none" stroke="#f6d313" stroke-width="1.1"/></svg>4-6 oz Filet Mignon</li>
      <li><svg viewBox="0 0 8 8"><rect x=".5" y=".5" width="7" height="7" fill="none" stroke="#f6d313"/><path d="M1.8 4l1.6 1.6L6.4 2" fill="none" stroke="#f6d313" stroke-width="1.1"/></svg>4-6 oz Flank Steak</li>
      <li><svg viewBox="0 0 8 8"><rect x=".5" y=".5" width="7" height="7" fill="none" stroke="#f6d313"/><path d="M1.8 4l1.6 1.6L6.4 2" fill="none" stroke="#f6d313" stroke-width="1.1"/></svg>4-6 oz Salmon</li>
      <li><svg viewBox="0 0 8 8"><rect x=".5" y=".5" width="7" height="7" fill="none" stroke="#f6d313"/><path d="M1.8 4l1.6 1.6L6.4 2" fill="none" stroke="#f6d313" stroke-width="1.1"/></svg>4-6 oz Tuna</li>
      <li><svg viewBox="0 0 8 8"><rect x=".5" y=".5" width="7" height="7" fill="none" stroke="#f6d313"/><path d="M1.8 4l1.6 1.6L6.4 2" fill="none" stroke="#f6d313" stroke-width="1.1"/></svg>4-6 oz Cod</li>
      <li><svg viewBox="0 0 8 8"><rect x=".5" y=".5" width="7" height="7" fill="none" stroke="#f6d313"/><path d="M1.8 4l1.6 1.6L6.4 2" fill="none" stroke="#f6d313" stroke-width="1.1"/></svg>4-6 oz Cottage Cheese</li>
      <li><svg viewBox="0 0 8 8"><rect x=".5" y=".5" width="7" height="7" fill="none" stroke="#f6d313"/><path d="M1.8 4l1.6 1.6L6.4 2" fill="none" stroke="#f6d313" stroke-width="1.1"/></svg>4-6 oz Greek Yogurt</li>
      <li><svg viewBox="0 0 8 8"><rect x=".5" y=".5" width="7" height="7" fill="none" stroke="#f6d313"/><path d="M1.8 4l1.6 1.6L6.4 2" fill="none" stroke="#f6d313" stroke-width="1.1"/></svg>4-6 oz Tofu</li>
      <li><svg viewBox="0 0 8 8"><rect x=".5" y=".5" width="7" height="7" fill="none" stroke="#f6d313"/><path d="M1.8 4l1.6 1.6L6.4 2" fill="none" stroke="#f6d313" stroke-width="1.1"/></svg>3 -5 egg whites +<br>1 whole egg</li>
    </ul>
  </section>

  <section class="food-col fat">
    <div class="col-icon" role="img" aria-label="Oil drops icon"><i style="background:#f0a91c"></i></div>
    <h2 class="col-head">FAT</h2>
    <ul class="food-list">
      <li><svg viewBox="0 0 8 8"><rect x=".5" y=".5" width="7" height="7" fill="none" stroke="#1c1c22"/><path d="M1.8 4l1.6 1.6L6.4 2" fill="none" stroke="#1c1c22" stroke-width="1.1"/></svg>¼ - ½ Avocado</li>
      <li><svg viewBox="0 0 8 8"><rect x=".5" y=".5" width="7" height="7" fill="none" stroke="#1c1c22"/><path d="M1.8 4l1.6 1.6L6.4 2" fill="none" stroke="#1c1c22" stroke-width="1.1"/></svg>1 tbs Olive Oil</li>
      <li><svg viewBox="0 0 8 8"><rect x=".5" y=".5" width="7" height="7" fill="none" stroke="#1c1c22"/><path d="M1.8 4l1.6 1.6L6.4 2" fill="none" stroke="#1c1c22" stroke-width="1.1"/></svg>1 small handful<br>Almonds, Walnuts,<br>Cashews</li>
    </ul>
  </section>

  <section class="food-col carbs">
    <div class="col-icon" role="img" aria-label="Rice bowl icon"><i style="background:#3d52a8"></i></div>
    <h2 class="col-head">CARBS</h2>
    <ul class="food-list">
      <li><svg viewBox="0 0 8 8"><rect x=".5" y=".5" width="7" height="7" fill="none" stroke="#fff"/><path d="M1.8 4l1.6 1.6L6.4 2" fill="none" stroke="#fff" stroke-width="1.1"/></svg>3 - 4oz Sweet Potato</li>
      <li><svg viewBox="0 0 8 8"><rect x=".5" y=".5" width="7" height="7" fill="none" stroke="#fff"/><path d="M1.8 4l1.6 1.6L6.4 2" fill="none" stroke="#fff" stroke-width="1.1"/></svg>¼ - ½ cup White Rice</li>
      <li><svg viewBox="0 0 8 8"><rect x=".5" y=".5" width="7" height="7" fill="none" stroke="#fff"/><path d="M1.8 4l1.6 1.6L6.4 2" fill="none" stroke="#fff" stroke-width="1.1"/></svg>¼ - ½ cup Quinoa</li>
      <li><svg viewBox="0 0 8 8"><rect x=".5" y=".5" width="7" height="7" fill="none" stroke="#fff"/><path d="M1.8 4l1.6 1.6L6.4 2" fill="none" stroke="#fff" stroke-width="1.1"/></svg>¼ - ½ cup Oatmeal</li>
      <li><svg viewBox="0 0 8 8"><rect x=".5" y=".5" width="7" height="7" fill="none" stroke="#fff"/><path d="M1.8 4l1.6 1.6L6.4 2" fill="none" stroke="#fff" stroke-width="1.1"/></svg>¾ cup Blueberries</li>
      <li><svg viewBox="0 0 8 8"><rect x=".5" y=".5" width="7" height="7" fill="none" stroke="#fff"/><path d="M1.8 4l1.6 1.6L6.4 2" fill="none" stroke="#fff" stroke-width="1.1"/></svg>¾ cup Strawberries</li>
      <li><svg viewBox="0 0 8 8"><rect x=".5" y=".5" width="7" height="7" fill="none" stroke="#fff"/><path d="M1.8 4l1.6 1.6L6.4 2" fill="none" stroke="#fff" stroke-width="1.1"/></svg>¾ cup Raspberries</li>
      <li><svg viewBox="0 0 8 8"><rect x=".5" y=".5" width="7" height="7" fill="none" stroke="#fff"/><path d="M1.8 4l1.6 1.6L6.4 2" fill="none" stroke="#fff" stroke-width="1.1"/></svg>1 med. Apple</li>
      <li><svg viewBox="0 0 8 8"><rect x=".5" y=".5" width="7" height="7" fill="none" stroke="#fff"/><path d="M1.8 4l1.6 1.6L6.4 2" fill="none" stroke="#fff" stroke-width="1.1"/></svg>1 small orange</li>
      <li><svg viewBox="0 0 8 8"><rect x=".5" y=".5" width="7" height="7" fill="none" stroke="#fff"/><path d="M1.8 4l1.6 1.6L6.4 2" fill="none" stroke="#fff" stroke-width="1.1"/></svg>1 small grapefruit</li>
    </ul>
  </section>

  <section class="food-col veg">
    <div class="col-icon" role="img" aria-label="Leafy greens icon"><i style="background:#2f8f3a"></i></div>
    <h2 class="col-head">VEGETABLES</h2>
    <ul class="food-list">
      <li><svg viewBox="0 0 8 8"><rect x=".5" y=".5" width="7" height="7" fill="none" stroke="#fff"/><path d="M1.8 4l1.6 1.6L6.4 2" fill="none" stroke="#fff" stroke-width="1.1"/></svg>1 Scoop Powdered<br>Greens</li>
      <li><svg viewBox="0 0 8 8"><rect x=".5" y=".5" width="7" height="7" fill="none" stroke="#fff"/><path d="M1.8 4l1.6 1.6L6.4 2" fill="none" stroke="#fff" stroke-width="1.1"/></svg>1 Cup Sautéed<br>Spinach</li>
      <li><svg viewBox="0 0 8 8"><rect x=".5" y=".5" width="7" height="7" fill="none" stroke="#fff"/><path d="M1.8 4l1.6 1.6L6.4 2" fill="none" stroke="#fff" stroke-width="1.1"/></svg>1 Cup Sautéed Kale,<br>Broccoli</li>
      <li><svg viewBox="0 0 8 8"><rect x=".5" y=".5" width="7" height="7" fill="none" stroke="#fff"/><path d="M1.8 4l1.6 1.6L6.4 2" fill="none" stroke="#fff" stroke-width="1.1"/></svg>1 Cup Sautéed Bell<br>Pepper</li>
      <li><svg viewBox="0 0 8 8"><rect x=".5" y=".5" width="7" height="7" fill="none" stroke="#fff"/><path d="M1.8 4l1.6 1.6L6.4 2" fill="none" stroke="#fff" stroke-width="1.1"/></svg>1 Cup Sautéed<br>Carrots</li>
      <li><svg viewBox="0 0 8 8"><rect x=".5" y=".5" width="7" height="7" fill="none" stroke="#fff"/><path d="M1.8 4l1.6 1.6L6.4 2" fill="none" stroke="#fff" stroke-width="1.1"/></svg>1 Cup Sautéed<br>Zucchini</li>
    </ul>
  </section>

  <div class="note"><b>NOTE:</b><span>&lt; 150 LBS STICK TO SMALLER PORTIONS</span><span>&gt; 150 LBS STICK TO LARGER PORTIONS.</span></div>

  <svg class="meal-wheel" style="left:40px" viewBox="0 0 120 120" aria-label="Breakfast: one carb, one protein, one vegetable">
    <g stroke="#fff" stroke-width="2">
      <path d="M11.5 32 A56 56 0 0 1 108.5 32 L89.4 43 A34 34 0 0 0 30.6 43 Z" fill="var(--carbs)"/>
      <path d="M108.5 32 A56 56 0 0 1 60 116 L60 94 A34 34 0 0 0 89.4 43 Z" fill="var(--protein)"/>
      <path d="M60 116 A56 56 0 0 1 11.5 32 L30.6 43 A34 34 0 0 0 60 94 Z" fill="var(--veg)"/>
    </g>
    <circle cx="60" cy="60" r="32" fill="#fff"/>
    <text x="60" y="64" text-anchor="middle" font-size="10.5" font-weight="800" fill="#1c1c22">BREAKFAST</text>
    <g fill="#fff" stroke="#1c1c22" stroke-width="1.5"><circle cx="60" cy="4" r="9"/><circle cx="11.5" cy="88" r="9"/><circle cx="108.5" cy="88" r="9"/></g>
    <g font-size="10" font-weight="800" fill="#1c1c22" text-anchor="middle"><text x="60" y="7.5">1</text><text x="11.5" y="91.5">1</text><text x="108.5" y="91.5">1</text></g>
  </svg>

  <div class="snack" style="left:183px">
    <svg width="56" height="26" viewBox="0 0 56 26"><path d="M6 24 C10 10 26 6 40 9 L38 2 L54 12 L36 20 L38 14 C26 12 14 15 6 24 Z" fill="#3b6fd0" stroke="#fff" stroke-width="1.2"/></svg>
    <span class="snack-tag">SNACK</span>
    <p>1/2 PORTION OF<br>PROTEIN</p>
  </div>

  <svg class="meal-wheel" style="left:280px" viewBox="0 0 120 120" aria-label="Lunch: one carb, one protein, one vegetable">
    <g stroke="#fff" stroke-width="2">
      <path d="M11.5 32 A56 56 0 0 1 108.5 32 L89.4 43 A34 34 0 0 0 30.6 43 Z" fill="var(--carbs)"/>
      <path d="M108.5 32 A56 56 0 0 1 60 116 L60 94 A34 34 0 0 0 89.4 43 Z" fill="var(--protein)"/>
      <path d="M60 116 A56 56 0 0 1 11.5 32 L30.6 43 A34 34 0 0 0 60 94 Z" fill="var(--veg)"/>
    </g>
    <circle cx="60" cy="60" r="32" fill="#fff"/>
    <text x="60" y="64" text-anchor="middle" font-size="10.5" font-weight="800" fill="#1c1c22">LUNCH</text>
    <g fill="#fff" stroke="#1c1c22" stroke-width="1.5"><circle cx="60" cy="4" r="9"/><circle cx="11.5" cy="88" r="9"/><circle cx="108.5" cy="88" r="9"/></g>
    <g font-size="10" font-weight="800" fill="#1c1c22" text-anchor="middle"><text x="60" y="7.5">1</text><text x="11.5" y="91.5">1</text><text x="108.5" y="91.5">1</text></g>
  </svg>

  <div class="snack" style="left:420px">
    <svg width="56" height="26" viewBox="0 0 56 26"><path d="M6 24 C10 10 26 6 40 9 L38 2 L54 12 L36 20 L38 14 C26 12 14 15 6 24 Z" fill="#3b6fd0" stroke="#fff" stroke-width="1.2"/></svg>
    <span class="snack-tag">SNACK</span>
    <p>1/2 PORTION OF<br>PROTEIN</p>
  </div>

  <svg class="meal-wheel" style="left:506px" viewBox="0 0 120 120" aria-label="Dinner: one fat, one protein, one vegetable">
    <g stroke="#fff" stroke-width="2">
      <path d="M11.5 32 A56 56 0 0 1 108.5 32 L89.4 43 A34 34 0 0 0 30.6 43 Z" fill="var(--fat)"/>
      <path d="M108.5 32 A56 56 0 0 1 60 116 L60 94 A34 34 0 0 0 89.4 43 Z" fill="var(--protein)"/>
      <path d="M60 116 A56 56 0 0 1 11.5 32 L30.6 43 A34 34 0 0 0 60 94 Z" fill="var(--veg)"/>
    </g>
    <circle cx="60" cy="60" r="32" fill="#fff"/>
    <text x="60" y="64" text-anchor="middle" font-size="10.5" font-weight="800" fill="#1c1c22">DINNER</text>
    <g fill="#fff" stroke="#1c1c22" stroke-width="1.5"><circle cx="60" cy="4" r="9"/><circle cx="11.5" cy="88" r="9"/><circle cx="108.5" cy="88" r="9"/></g>
    <g font-size="10" font-weight="800" fill="#1c1c22" text-anchor="middle"><text x="60" y="7.5">1</text><text x="11.5" y="91.5">1</text><text x="108.5" y="91.5">1</text></g>
  </svg>

  <div class="fuel-band"><span>FUEL YOUR</span><span>CORAL TIDE!</span></div>
  <p class="fuel-copy">This plan isn't about starving yourself - it's about sculpting a lean, toned physique by shredding fat while preserving muscle.</p>

  <section class="tips">
    <article class="tip"><span class="tip-num">1</span><h3>Eat Like a Champion</h3><p>Stick to this list as close as possible for maximum results, 7 Days A Week</p></article>
    <article class="tip"><span class="tip-num">2</span><h3>Burn More Than You Consume</h3><p>This is the golden rule! You need to burn more calories than you consume to create a deficit and force your body to tap into fat</p></article>
    <article class="tip"><span class="tip-num">3</span><h3>Prioritize Protein</h3><p>Protein helps build and maintain muscle mass, which is crucial for boosting metabolism and burning more calories at rest.</p></article>
    <article class="tip"><span class="tip-num">4</span><h3>Maximize Sleep</h3><p>When sleep-deprived, your body produces more ghrelin (hunger hormone) and less leptin (satiety hormone). Aim for 7-8 hrs of quality sleep nightly</p></article>
    <article class="tip"><span class="tip-num">5</span><h3>Consistency is King/Queen</h3><p>Don't expect overnight results. Stick to your plan, track your progress, and celebrate small victories. Remember, slow and steady wins the shred race</p></article>
  </section>
</main>
</body>
</html>
```